light box menu and wall graphics

HI My name is Derek Halvorsen and I am putting together a Pebble Mugs franchise. We are a high quaulity coffee offering and the retail concept is for a in-line store in a busy shopping centre food court. We are a highly visible coffee offering with vibrant bright orange colour (pantone 021 / process m60_y100)
Orange might make a good background on the menu board as it needs to blend in with colour scheme. Also the text has to be at least 15ml and not too busy but clearly legible. The font is: Akzent Rounded
The twin light boxes being used is from http://www.glowpanelstore.example.au/pg/lightboxes/new/sdb/light-box-1560S.aspx
They measure in total 3m wide X .6 height

There are two elements to this job, one is the twin menu boards and the other is the wall graphic.
please see wall graphic examples attached.
This graphic is to be painted onto the wall by a sign writter.
The design to go on the wall needs to be a synonymous with our quality coffee vison and match the shop design, I have examples of the type of wall art I am after attached. I was thinking somehow a Cart with wings would look neat and we could incorportate some text into it. Such as "Brew with Heart puts a smile on you" and "Genuine Mug" Flames could look amazing too!

My website is unfortunately down at the moment but I am attaching plenty

I have just added the menu in easy to read updated format.
Thanks to those who have expressed interest!
Updates

Hi Designers, I have just increased first prize by $100.00

Please note the signage boards run horizontally not vertically.  I have also added more artwork.

thanks

Derek

 HI there, thanks for joining.  I have just updated the brief to make it as clear as possible.

Hope you enjoy this experience.  I am here to answer any questions.

Derek

Thank you for accepting my invitation for this design job.

Look forward to seeing some designs as per brief.

Need to have this finished by Friday the 19th of October.  Thanks

Target Market(s)

Coffee lovers, kids who want hot chocolates, frappes,
etc

Industry/Entity Type

Shopping

Requirements
Must have
• Must have coffee in it for clarity.
Also in the menu any images of food or drink must be photo/posters attached

```html
<!DOCTYPE html>
<html lang="en">
<head>
<meta charset="utf-8">
<title>Pebble Mugs – Menu Board</title>
<link rel="stylesheet" href="https://fonts.googleapis.com/css2?family=Nunito:wght@400;600;800;900&display=swap">
<style>
  :root {
    --page: #efe9e3;
    --board-deep: #b85a1e;
    --board-mid: #d9793a;
    --board-light: #eb9a5a;
    --panel: rgba(246, 178, 112, 0.55);
    --ink: #3b1606;
    --ink-soft: #4a200c;
    --rule: rgba(80, 30, 8, 0.45);
  }
  * { box-sizing: border-box; margin: 0; padding: 0; }
  html, body {
    width: 1200px; height: 1000px; overflow: hidden;
    background: var(--page);
    font-family: "Nunito", "Arial Rounded MT Bold", sans-serif;
    color: var(--ink);
  }
  .menu-board {
    position: absolute; left: 0; top: 318px;
    width: 1200px; height: 365px; overflow: hidden;
    background: linear-gradient(100deg, var(--board-deep) 0%, var(--board-mid) 40%, var(--board-light) 70%, var(--board-mid) 100%);
  }
  .photo { position: absolute; }
  .photo--cup {
    left: 0; top: 0; width: 300px; height: 365px;
    background: radial-gradient(ellipse at 35% 35%, #f0b27c 0%, #c5692c 45%, #7a3510 100%);
    opacity: .85;
  }
  .photo--frappe {
    left: 880px; top: 0; width: 320px; height: 200px;
    background: radial-gradient(ellipse at 55% 40%, #f6c089 0%, #df8a47 55%, rgba(217,121,58,0) 100%);
  }
  .panel {
    position: absolute; top: 60px; height: 270px; background: var(--panel);
  }
  .panel--coffee { left: 38px; width: 537px; }
  .panel--frappes { left: 623px; width: 537px; }
  .divider {
    position: absolute; left: 603px; top: 30px; width: 1px; height: 320px; background: var(--rule);
  }
  .section-title {
    position: absolute; font-weight: 800; font-size: 29px; line-height: 1;
  }
  .section-title--coffee { left: 52px; top: 22px; }
  .section-title--frappes { left: 637px; top: 22px; }
  .sizes { position: absolute; top: 18px; display: flex; gap: 20px; font-weight: 800; }
  .sizes--coffee { left: 300px; }
  .sizes--frappes { left: 930px; }
  .size { text-align: center; line-height: 1; }
  .size__main { font-size: 22px; white-space: nowrap; }
  .size__main small { font-size: 15px; }
  .size__note { display: block; font-size: 10px; font-weight: 600; margin-top: 2px; }
  .item-list { position: absolute; list-style: none; font-weight: 800; font-size: 26px; line-height: 39px; }
  .item-list--coffee { left: 53px; top: 75px; }
  .item-list--frappes { left: 639px; top: 75px; }
  .extras { position: absolute; list-style: none; font-size: 14px; line-height: 22.5px; color: var(--ink-soft); }
  .extras li { font-weight: 800; }
  .extras li::before { content: "•"; display: inline-block; width: 18px; }
  .extras .light { font-weight: 400; }
  .extras--coffee { left: 347px; top: 123px; }
  .extras--frappes { left: 880px; top: 164px; }
  .single-price { position: absolute; left: 346px; top: 76px; font-weight: 800; font-size: 26px; line-height: 1; }
  .single-price small { font-size: 14px; vertical-align: top; margin-right: 4px; }
  .surcharge { position: absolute; font-weight: 800; font-size: 13px; }
  .surcharge--coffee { left: 347px; top: 103px; }
  .surcharge--frappes { left: 880px; top: 145px; }
  .iced-list { position: absolute; left: 879px; top: 72px; list-style: none; font-weight: 800; font-size: 26px; line-height: 39px; }
  .iced-list small { font-size: 10px; font-weight: 600; margin-left: 2px; }
  .brand {
    position: absolute; left: 1000px; top: 300px;
    font-weight: 900; font-size: 26px; line-height: 1; color: var(--ink);
  }
</style>
</head>
<body>
  <section class="menu-board" aria-label="Pebble Mugs menu board">
    <div class="photo photo--cup" role="img" aria-label="Photo of a cappuccino cup with saucer"></div>
    <div class="photo photo--frappe" role="img" aria-label="Photo of an iced frappe topped with cream"></div>

    <div class="panel panel--coffee"></div>
    <div class="panel panel--frappes"></div>
    <div class="divider"></div>

    <h2 class="section-title section-title--coffee">Coffee</h2>
    <div class="sizes sizes--coffee">
      <div class="size"><span class="size__main">S <small>$</small>3<small>.80</small></span><span class="size__note">(1 Shot)</span></div>
      <div class="size"><span class="size__main">M <small>$</small>4<small>.50</small></span><span class="size__note">(2 Shot)</span></div>
      <div class="size"><span class="size__main">L <small>$</small>4<small>.90</small></span><span class="size__note">(2 Shot)</span></div>
    </div>
    <ul class="item-list item-list--coffee">
      <li>Espresso Shot</li><li>Long Black</li><li>Flat White</li>
      <li>Latte</li><li>Cappuccino</li><li>Hot Chocolate</li>
    </ul>
    <div class="single-price"><small>$</small>2.90</div>
    <div class="surcharge surcharge--coffee">+&nbsp;&nbsp; 50¢</div>
    <ul class="extras extras--coffee">
      <li>Soy</li><li>Mocha</li><li>Vienna</li><li>Decaf (fresh)</li>
      <li>Syrups; <span class="light">vanilla, caramel, hazelnut</span></li>
      <li>Cream</li><li>Coffee shot</li><li>White chocolate</li>
    </ul>

    <h2 class="section-title section-title--frappes">Frappes</h2>
    <div class="sizes sizes--frappes">
      <div class="size"><span class="size__main">M <small>$</small>5<small>.00</small></span></div>
      <div class="size"><span class="size__main">L <small>$</small>5<small>.50</small></span></div>
    </div>
    <ul class="item-list item-list--frappes">
      <li>Vanilla</li><li>Hazelnut</li><li>Caramel</li>
      <li>Chocolate</li><li>Coffee</li><li>Chai</li>
    </ul>
    <ul class="iced-list">
      <li>Iced Chocolate<small>1 scoop ice cream</small></li>
      <li>Iced Coffee<small>1 scoop ice cream</small></li>
    </ul>
    <div class="surcharge surcharge--frappes">+&nbsp;&nbsp; 50¢</div>
    <ul class="extras extras--frappes">
      <li>Mocha</li><li>Cream</li>
      <li>Syrups; <span class="light">vanilla, caramel, hazelnut</span></li>
    </ul>

    <div class="brand">Pebble Mugs</div>
  </section>
</body>
</html>
```